Criação de Embalagem (unidade) para Viagens & Lazer
" Produzimos e importamos produtos náuticos e comercializamos para os públicos citados a seguir. Além disso, prestamos suporte na instalação e uso dos produtos. "

```html
<!DOCTYPE html>
<html lang="pt-BR">
<head>
<meta charset="UTF-8">
<title>Maréa Náutica — Embalagem Hélice</title>
<link href="https://fonts.googleapis.com/css2?family=Montserrat:wght@400;500;800&display=swap" rel="stylesheet">
<style>
  :root {
    --page: #ffffff;
    --teal-top: #1d5565;
    --teal-mid: #245f70;
    --teal-deep: #163f4c;
    --ink-light: #ffffff;
    --ink-soft: #e6f0f2;
    --prop: #f4f6f6;
  }
  * { margin: 0; padding: 0; box-sizing: border-box; }
  html, body {
    width: 1200px; height: 1200px; overflow: hidden;
    background: var(--page);
    font-family: "Montserrat", sans-serif;
  }
  .pack-panel {
    position: absolute; left: 319px; top: 0;
    width: 560px; height: 1200px;
    background: linear-gradient(180deg, var(--teal-top) 0%, var(--teal-mid) 55%, var(--teal-deep) 100%);
    color: var(--ink-light);
    overflow: hidden;
  }
  .brand-name {
    position: absolute; top: 52px; left: 0; width: 100%;
    text-align: center;
    font-size: 36px; font-weight: 500; letter-spacing: 6px;
    color: var(--ink-light);
  }
  .section-title {
    position: absolute; left: 58px;
    font-size: 18px; font-weight: 800; letter-spacing: 0.5px;
    text-transform: uppercase; line-height: 1.4;
  }
  .install-title { top: 200px; }
  .install-text {
    position: absolute; left: 58px; top: 260px;
    font-size: 17px; font-weight: 400; line-height: 25px;
    white-space: nowrap;
    color: var(--ink-soft);
  }
  .install-diagram {
    position: absolute; left: 58px; top: 488px;
    width: 420px; height: 172px;
    background: linear-gradient(90deg, rgba(223,232,235,0.10), rgba(223,232,235,0.22));
    border-radius: 6px;
  }
  .know-title { top: 716px; }
  .prop-diagram {
    position: absolute; left: 250px; top: 696px;
    width: 290px; height: 96px;
    background: rgba(223,232,235,0.16);
    border-radius: 6px;
  }
  .photo-band {
    position: absolute; left: 0; top: 808px;
    width: 100%; height: 392px;
    background: linear-gradient(180deg, #2a6474 0%, #3c7482 40%, #1b4856 100%);
  }
  .propeller-photo {
    position: absolute; left: 40px; top: 860px;
    width: 230px; height: 360px;
    border-radius: 110px 110px 0 0;
    background: linear-gradient(160deg, #ffffff 0%, var(--prop) 50%, #cfd8da 100%);
  }
  .handling-icons {
    position: absolute; left: 240px; top: 840px;
  }
</style>
</head>
<body>
  <main class="pack-panel">
    <div class="brand-name">MARÉA NÁUTICA</div>

    <h2 class="section-title install-title">Instalação</h2>
    <p class="install-text">
      Remova os cabos e/ou cabos de vela, antes de<br>
      manusear a Hélice.<br>
      O desenho abaixo mostra a ordem de instala-<br>
      ção, podendo variar de acordo com o modelo e<br>
      a marca do motor.<br>
      sempre que possível consulte o manual do pro-<br>
      prietário e/ou o manual técnico do motor
    </p>

    <div class="install-diagram" role="img" aria-label="Desenho técnico da ordem de montagem da hélice no eixo: eixo, encosto, hélice, espaçador, arruela, porca e cupilha"></div>

    <h2 class="section-title know-title">Conheça a hélice<br>do seu motor.</h2>
    <div class="prop-diagram" role="img" aria-label="Desenho técnico indicando diâmetro, raio, passo e sentido de rotação da hélice"></div>

    <div class="photo-band" role="img" aria-label="Fotografia de um barco na água em tons de azul petróleo"></div>
    <div class="propeller-photo" role="img" aria-label="Fotografia da hélice branca de três pás com cubo metálico"></div>

    <svg class="handling-icons" width="300" height="56" viewBox="0 0 300 56" fill="none" stroke="#ffffff" stroke-width="3" aria-label="Símbolos de manuseio">
      <path d="M10 44 V14 M3 22 L10 12 L17 22 M30 44 V14 M23 22 L30 12 L37 22"/>
      <path d="M2 50 H38"/>
      <text x="80" y="22" fill="#ffffff" stroke="none" font-family="Montserrat, sans-serif" font-weight="800" font-size="20" text-anchor="middle">6</text>
      <path d="M62 30 H98 M62 38 H98 M62 46 H98"/>
      <path d="M136 26 Q156 4 176 26 Z" fill="#ffffff"/>
      <path d="M156 26 V44 Q156 50 150 48"/>
      <path d="M142 34 v4 M170 34 v4" stroke-width="2"/>
      <path d="M214 10 H236 Q236 30 225 32 Q214 30 214 10 Z M225 32 V46 M217 48 H233"/>
      <path d="M222 14 L227 20 L223 25" stroke-width="2"/>
    </svg>
  </main>
</body>
</html>
```